PREMIUM AGENCY High End Business Card - A+++ Designers Wanted

** DO NOT ATTEMPT TO CONTACT ME THROUGH SEARCHING ON ZINTREL OR EMAILING ME THROUGH MY WEBSITE **

I need a fresh, contemporary business card designed using the logo attached (BRONSALK)

I have attached the font for BRONSALK

It must have a premium look and feel. The business card size must be STANDARD size.

You can submit either/both VERTICAL or HORIZONTAL designs.

FRONT: It must have the following sample information on

Paul Ardley
Director Operations
Mobile +61 452 118 906
Email paulardley@bronsalk.com
www.bronsalk.com

The REAR of the business card must have the words

CREATE INSPIRE TOMORROW

as part of the design, in the same font (NEXA) attached.

The words do not need to be in capitals, or on the same line, please design this as you see it best working.

ADDITIONAL INFORMATION
======================

The BRONSALK logo must be on the front of the card

I want Ultraviolet printing on the final design, to enhance either the NAME of the person OR the BRONSALK logo OR the words on the back of the card.

Target Market(s)

Agency, Advertising Agency, Creative, Designers

Industry/Entity Type

Media

Contact Information for Business Card

Design Agency, Contemporary, Premium look and feel, High Quality

Font styles to use
Serif
Sans Serif
Other font styles liked:
• ATTACHED TO PROJECT

Requirements
Must have
• BLACK & WHITE as the primary design, and if you feel there can be a highlighted colour, then this can be used.
• The Logo ICON attached is blue, this colour must not be changed.
• I have attached the partner brand BRONSALK MEDIA incase you need to manipulate the original files.
• ** DO NOT ATTEMPT TO CONTACT ME THROUGH SEARCHING ON ZINTREL OR EMAILING ME THROUGH MY WEBSITE **
Nice to have
• Must be Premium. I have attached some sample designs, that I like that would be a good inspiration for where this can be taken.
• My favourite design is is the KESTRAVUE2-BUSINESSCARD-TEMPLATE
Should not have
• No funny or silly standard / off the shelf designs

```html
<!DOCTYPE html>
<html lang="en">
<head>
<meta charset="utf-8">
<title>Bronsalk Media – Business Card</title>
<link rel="stylesheet" href="https://fonts.googleapis.com/css2?family=Montserrat:wght@300;400;600;700&display=swap">
<style>
  :root {
    --brand-blue: #25a7df;
    --ink: #1c1c1c;
    --paper: #ffffff;
    --backdrop: #e9eaec;
    --muted: #3a3a3a;
  }
  * { margin: 0; padding: 0; box-sizing: border-box; }
  html, body { width: 1200px; height: 891px; overflow: hidden; }
  body {
    background: var(--backdrop);
    font-family: "Montserrat", Arial, sans-serif;
    color: var(--ink);
    position: relative;
  }
  .card {
    position: absolute;
    top: 297px;
    width: 520px;
    height: 297px;
    background: var(--paper);
    overflow: hidden;
    box-shadow: 0 6px 18px rgba(0,0,0,0.12);
  }
  /* Front: contact side */
  .card--front { left: 60px; }
  .front__panel {
    position: absolute;
    left: 0; top: 0;
    width: 212px; height: 100%;
    background: var(--brand-blue);
  }
  .front__details {
    position: absolute;
    left: 246px; top: 62px;
  }
  .person__name {
    font-size: 29px;
    font-weight: 700;
    letter-spacing: 0.2px;
    line-height: 1;
  }
  .person__role {
    margin-top: 8px;
    font-size: 14px;
    font-weight: 300;
    letter-spacing: 0.6px;
    color: var(--muted);
  }
  .contact-list {
    list-style: none;
    margin-top: 30px;
  }
  .contact-list__item {
    display: flex;
    align-items: center;
    gap: 12px;
    font-size: 13px;
    font-weight: 400;
    color: var(--muted);
    margin-bottom: 11px;
  }
  .contact-list__icon {
    width: 20px; height: 20px;
    flex: none;
  }
  /* Back: tagline side */
  .card--back { left: 620px; }
  .back__logo {
    position: absolute;
    left: 0; right: 0; top: 96px;
    display: flex;
    justify-content: center;
    align-items: center;
    gap: 14px;
  }
  .logo__dot {
    width: 22px; height: 22px;
    border-radius: 50%;
    background: var(--brand-blue);
  }
  .logo__name {
    font-size: 26px;
    font-weight: 700;
    letter-spacing: 3px;
    color: var(--ink);
  }
  .back__band {
    position: absolute;
    left: 0; bottom: 0;
    width: 100%; height: 66px;
    background: var(--brand-blue);
    display: flex;
    justify-content: space-between;
    align-items: center;
    padding: 0 30px;
  }
  .tagline__word {
    color: var(--paper);
    font-size: 14px;
    font-weight: 700;
    letter-spacing: 1.5px;
  }
</style>
</head>
<body>
  <section class="card card--front" aria-label="Business card front">
    <div class="front__panel"></div>
    <div class="front__details">
      <h1 class="person__name">Paul Ardley</h1>
      <p class="person__role">Director Operations</p>
      <ul class="contact-list">
        <li class="contact-list__item">
          <svg class="contact-list__icon" viewBox="0 0 20 20" aria-hidden="true">
            <rect width="20" height="20" fill="#1c1c1c"/>
            <rect x="6.5" y="3.5" width="7" height="13" rx="1" fill="none" stroke="#fff" stroke-width="1.5"/>
            <circle cx="10" cy="14" r="0.9" fill="#fff"/>
          </svg>
          +61 452 118 906
        </li>
        <li class="contact-list__item">
          <svg class="contact-list__icon" viewBox="0 0 20 20" aria-hidden="true">
            <rect width="20" height="20" fill="#1c1c1c"/>
            <rect x="4" y="6" width="12" height="8" fill="none" stroke="#fff" stroke-width="1.4"/>
            <path d="M4 6 L10 11 L16 6" fill="none" stroke="#fff" stroke-width="1.4"/>
          </svg>
          paulardley@bronsalk.com
        </li>
        <li class="contact-list__item">
          <svg class="contact-list__icon" viewBox="0 0 20 20" aria-hidden="true">
            <rect width="20" height="20" fill="#1c1c1c"/>
            <circle cx="10" cy="10" r="5.5" fill="none" stroke="#fff" stroke-width="1.3"/>
            <ellipse cx="10" cy="10" rx="2.3" ry="5.5" fill="none" stroke="#fff" stroke-width="1.1"/>
            <line x1="4.5" y1="10" x2="15.5" y2="10" stroke="#fff" stroke-width="1.1"/>
          </svg>
          www.bronsalk.com
        </li>
      </ul>
    </div>
  </section>

  <section class="card card--back" aria-label="Business card back">
    <div class="back__logo">
      <span class="logo__dot"></span>
      <span class="logo__name">BRONSALK MEDIA</span>
    </div>
    <div class="back__band">
      <span class="tagline__word">CREATE</span>
      <span class="tagline__word">INSPIRE</span>
      <span class="tagline__word">TOMORROW</span>
    </div>
  </section>
</body>
</html>
```